A corporate website

The target design is for Vellmar Glassworks coporate site which is a major international manufacturers for the finest quality of transparent and colored full lead crystal (more than 30% PbO)

Vellmar Glassworks is the largest producer of crystal in world with 98% of its production exported to more than 120 countries.

Vellmar Glassworks has 4 business lines:
1. Crystal Fashion Components
2. Chandeliers Crystal Parts
3. Lighting Collection and special design
4. Gifts and accessories

The winner bidder(s) would be asked to do more jobs

The corporate website is the official site that represents Vellmar HQ in front of world and it includes the following pages:
1. Home page
2. Facilities:
a. Factories overview
b. Factories image and video gallery
c. Show rooms locator
d. Quality Control
3. Media Center with the following sub pages
a. Press releases (Previous and future press releases)
b. Logos & artwork (Hi res images for Vellmar Glassworks to be used by various worldwide media)
c. Media contacts (contacts of Vellmar’s media division)
4. Careers:
a. Publish opened positions from Pindle hire
b. Capture candidates resumes using Pindle hire form
5. About US

Target Market(s)

Business partners, resellers, end customers, press and employees

Industry/Entity Type

Business

Requirements
Must have
• The design should include a home webpage and an internal page design. The design should fullfill the following requriements:

1. Strictly follow the corporate identity materials guidelines - see attachment
2. Supports multi-language
3. User can change between languages using flags
4. Web surfer can optionally change the default language
5. An integrated live chat push button for ChatBrio
8. Site Header should contain the following information:
a. Logo
b. Slogan
c. Links to site pages
d. Link to the home page
e. Link to the landing page
f. A language option drop box
9. Footers should have:
a. Links to all other 5 websites in a dropbox form
b. Link to privacy statement
c. Link to copyright notice
d. Link to sitemap
e. Newsletter subscription one field form
11. Every sub-site should have a universal customer service section that offer the following services:
a. Links to end user installation manuals
b. Links to products cleaning and maintenance guide
c. Customer complaints center
12. A news sub-section that should contain:
a. Latest product and promotional announcements
b. Corporate news
c. Exhibitions coverage
13. A link to vellmar Worldwide:
a. A database driven interactive map reflecting Vellmar list of agents and distributors worldwide with list of supported products this interactive map could be limited in every sub-site for specific line of product
b. Capture potential resellers and agents
c. Become a partner form

```html
<!DOCTYPE html>
<html lang="en">
<head>
<meta charset="utf-8">
<title>Vellmar Glassworks – Home</title>
<link rel="stylesheet" href="https://fonts.googleapis.com/css2?family=Arimo:wght@400;700&family=PT+Sans&family=Cinzel:wght@700&display=swap">
<style>
:root{
  --page:#22242e;
  --page-dark:#1b1d26;
  --panel:#2b2e3b;
  --panel-hi:#3a3e4e;
  --rule:#6e7486;
  --white:#ffffff;
  --frame:#d4d7ef;
  --frame-edge:#b4b8dc;
  --nav:#dfe3f6;
  --nav-active:#a9b1cf;
  --text-light:#e8e9ef;
  --text-muted:#b8bbc7;
  --red:#cc2200;
  --link-red:#e23b1a;
  --card-border:#d5d5d5;
  --chat-top:#7fc4ff;
  --chat-bot:#1a6fe0;
}
*{box-sizing:border-box;margin:0;padding:0}
html,body{width:845px;height:1200px;overflow:hidden}
body{background:var(--page);font-family:"Arimo",Arial,sans-serif;color:var(--text-light);position:relative}
a{color:inherit;text-decoration:none}
.abs{position:absolute}

/* header */
.site-header{position:absolute;left:0;top:0;width:845px;height:116px;background:linear-gradient(#262833,#1f2129)}
.brand{position:absolute;left:20px;top:11px;width:150px;height:106px;background:var(--white);border-radius:10px 10px 0 0;display:flex;flex-direction:column;align-items:center;justify-content:center;gap:6px}
.brand-mark{width:28px;height:28px;border-radius:50%;background:#9a9ca4}
.brand-name{font-family:"PT Sans",sans-serif;font-size:15px;color:#5a5c63;letter-spacing:1px;text-align:center;line-height:1.1}
.util-links{position:absolute;right:20px;top:12px;font-size:11px;color:var(--text-muted);display:flex;gap:14px}
.lang{position:absolute;right:19px;top:46px;font-size:11px;color:var(--text-muted)}
.main-nav{position:absolute;left:192px;top:77px;width:477px;height:39px;background:linear-gradient(#f1f3fb,var(--nav));border:1px solid var(--frame-edge);border-radius:4px 4px 0 0;display:flex;align-items:stretch;padding-left:10px}
.main-nav a{font-size:11px;color:#111;display:flex;align-items:center;justify-content:center}
.main-nav a.active{background:linear-gradient(#c6cce4,var(--nav-active));width:66px;margin-top:2px}
.search{position:absolute;left:680px;top:86px;width:148px;height:17px;background:#3c404f;border:1px solid #55596a;font-size:10px;color:#8f93a3;padding:2px 12px}
.search-btn{position:absolute;right:0;top:0;width:22px;height:15px;background:#b9bcc7}

/* hero */
.hero{position:absolute;left:0;top:116px;width:845px;height:330px;background:linear-gradient(#1e2029,#252834);border-top:1px solid #4a4e5e;border-bottom:1px solid #4a4e5e}
.hero-frame{position:absolute;left:62px;top:31px;width:726px;height:270px;background:var(--frame);border-radius:10px;border:1px solid var(--frame-edge)}
.hero-photo{position:absolute;left:18px;top:16px;width:688px;height:235px;background:radial-gradient(circle at 25% 35%,#e6e6e6,#9a9a9a 40%,#6a6a6a 80%)}
.hero-arrow{position:absolute;top:195px;width:36px;height:47px;background:var(--white);border-radius:4px;display:flex;align-items:center;justify-content:center}

/* columns */
.side{position:absolute;top:447px;width:168px}
.side-head{height:36px;background:linear-gradient(var(--panel-hi),var(--panel));border:1px solid #4b4f60;font-family:"Cinzel",serif;font-size:9.5px;color:var(--white);display:flex;align-items:center;padding-left:12px;gap:10px;line-height:1.2}
.side-head::before{content:"";width:8px;height:8px;border-radius:2px;background:#dfe2ee;flex:none}
.cat-list{list-style:none;font-family:"PT Sans",sans-serif;font-size:10.5px}
.cat-list li{height:21px;display:flex;align-items:center;padding-left:12px;gap:16px}
.cat-list li::before{content:"›";font-weight:700;font-size:13px}
.cat-list li.current{background:#3d404e}
.news-item{padding:0 10px 0 12px;font-size:11px;line-height:1.25}
.news-date{display:inline-block;background:#4d505c;color:#9fa2ae;font-size:10px;padding:1px 6px;width:68px;margin-bottom:4px}
.read-more{color:var(--link-red);text-decoration:underline;font-size:9px;display:block;margin-top:6px}
.thumb-row{display:flex;gap:8px;align-items:flex-start;font-size:11px;line-height:1.2}
.thumb{width:33px;height:34px;border:2px solid #ddd;background:radial-gradient(circle,#d8b9d2,#8a6c84);flex:none}
.more{display:block;text-align:right;color:var(--link-red);text-decoration:underline;font-size:9px}

.center{position:absolute;left:185px;top:447px;width:476px;height:580px;background:var(--white)}
.sec-head{position:absolute;left:3px;width:469px;height:40px;background:linear-gradient(#3a3e4c,#20222c);font-family:"PT Sans",sans-serif;font-size:17px;color:var(--white);display:flex;align-items:center;padding-left:11px}
.card{position:absolute;width:126px;height:168px;border:1px solid var(--card-border);box-shadow:1px 2px 3px #bbb;background:var(--white)}
.card-photo{position:absolute;left:4px;top:3px;width:118px;height:105px;border:5px solid #111}
.card-photo.red{background:radial-gradient(circle at 50% 50%,#c98a8a,#6b1010 45%,#3a0000)}
.card-photo.clear{background:radial-gradient(circle,#f0f0f0,#9a9a9a 45%,#111 75%)}
.card-photo.violet{background:radial-gradient(circle at 50% 40%,#d9d2ff,#6f63b8 45%,#201830)}
.card-title{position:absolute;left:16px;top:117px;color:var(--red);font-weight:700;font-size:11px}
.card-text{position:absolute;left:17px;top:131px;color:#111;font-size:9.5px;line-height:1.2}
.pager{position:absolute;font-size:18px;color:#999}

.login label{display:block;font-size:11px;margin:0 0 4px 0}
.field{width:131px;height:17px;background:#3d404e;border:1px solid #5a5e6e;margin-bottom:10px}
.chat-btn{position:absolute;left:675px;top:872px;width:145px;height:36px;border-radius:18px;background:linear-gradient(var(--chat-top),var(--chat-bot));border:1px solid #0d4fa8;font-family:"PT Sans",sans-serif;font-size:12px;color:var(--white);display:flex;align-items:center;justify-content:center}

/* footer */
.site-footer{position:absolute;left:0;top:1027px;width:845px;height:173px;background:var(--page-dark);border-top:2px solid #4a4e5e;font-size:11px}
.f-col{position:absolute;top:26px}
.f-col h4{font-size:11px;font-weight:700;color:var(--white);margin-bottom:10px}
.f-col ul{list-style:none}
.f-col li{line-height:21px}
.f-col.arrows li{padding-left:11px;position:relative}
.f-col.arrows li::before{content:"›";position:absolute;left:0;font-weight:700}
.f-col.sites li{text-decoration:underline}
.social{position:absolute;left:714px;top:1146px;display:flex;gap:4px}
.social span{width:30px;height:30px;border-radius:4px;background:#3b6fc2;font-size:7px;display:flex;align-items:center;justify-content:center;color:var(--white)}
.social span.feed{background:#e98a1c}
</style>
</head>
<body>

<header class="site-header">
  <a class="brand" href="#"><span class="brand-mark"></span><span class="brand-name">VELLMAR<br>GLASSWORKS</span></a>
  <nav class="util-links"><a href="#">My Account</a><a href="#">Track Order</a><a href="#">Quick Order</a></nav>
  <div class="lang">English | Danish</div>
  <nav class="main-nav">
    <a class="active" href="#">Home</a>
    <a href="#" style="width:100px">Facilities</a>
    <a href="#" style="width:100px">Media Center</a>
    <a href="#" style="width:88px">Careers</a>
    <a href="#" style="width:104px">About Us</a>
  </nav>
  <div class="search">Search<span class="search-btn"></span></div>
</header>

<section class="hero">
  <div class="hero-frame">
    <div class="hero-photo" role="img" aria-label="Clear crystal spheres on crystal stands, golf ball and engraved globe"></div>
  </div>
  <a class="hero-arrow" href="#" style="left:52px"><svg width="10" height="14"><path d="M8 1 2 7l6 6z" fill="#888"/></svg></a>
  <a class="hero-arrow" href="#" style="left:760px"><svg width="10" height="14"><path d="M2 1l6 6-6 6z" fill="#888"/></svg></a>
</section>

<!-- left column -->
<aside class="side" style="left:17px">
  <div class="side-head" style="margin-top:8px">Shop by Category</div>
  <ul class="cat-list" style="margin-top:1px">
    <li class="current">Crystal Fashion Components</li>
    <li>Chandeliers Crystal Parts</li>
    <li>Lighting Collection</li>
    <li>Special design</li>
    <li>Gifts &amp; accessories</li>
  </ul>
  <div class="side-head" style="margin-top:22px;height:28px">Corporate News</div>
  <div class="news-item" style="margin-top:3px;border-top:1px solid var(--rule)">
    <span class="news-date">29 november</span>
    <p>Lorem ipsum dolor sit amet, sectetu adip scing varius interdum incid unt quis, libero. Aenean mturpis.</p>
    <a class="read-more" href="#">read more</a>
  </div>
  <div class="news-item" style="margin-top:11px;border-top:1px solid var(--rule)">
    <span class="news-date">29 november</span>
    <p>Lorem ipsum dolor sit amet, sectetu adip scing varius interdum incid unt quis, libero. Aenean mturpis.</p>
    <a class="read-more" href="#">read more</a>
  </div>
  <div class="side-head" style="margin-top:22px;height:38px">Promotional<br>Announcements</div>
  <div class="thumb-row" style="margin:10px 0 0 18px"><span class="thumb"></span><p>Lorem ipsum dolor sit amet, sectetu<a class="more" href="#">more</a></p></div>
  <div class="thumb-row" style="margin:10px 0 0 18px"><span class="thumb"></span><p>Lorem ipsum dolor sit amet, sectetu<a class="more" href="#">more</a></p></div>
</aside>

<!-- center -->
<main class="center">
  <h2 class="sec-head" style="top:9px">Crystal Fashion Components</h2>
  <article class="card" style="left:13px;top:71px"><div class="card-photo red" role="img" aria-label="Red crystal sphere"></div><h3 class="card-title">Neque porro</h3><p class="card-text">who seeks after it and<br>wants to have it.</p></article>
  <article class="card" style="left:175px;top:71px"><div class="card-photo clear" role="img" aria-label="Clear crystal sphere with etched figure"></div><h3 class="card-title">Neque porro</h3><p class="card-text">who seeks after it and<br>wants to have it.</p></article>
  <article class="card" style="left:335px;top:71px"><div class="card-photo violet" role="img" aria-label="Violet crystal globe on stand"></div><h3 class="card-title">Neque porro</h3><p class="card-text">who seeks after it and<br>wants to have it.</p></article>
  <svg class="pager" style="left:18px;top:260px" width="10" height="12"><path d="M8 1 2 6l6 5" stroke="#999" stroke-width="2.5" fill="none"/></svg>
  <svg class="pager" style="left:451px;top:260px" width="10" height="12"><path d="M2 1l6 5-6 5" stroke="#999" stroke-width="2.5" fill="none"/></svg>

  <h2 class="sec-head" style="top:288px">Chandeliers Crystal Parts</h2>
  <article class="card" style="left:13px;top:350px"><div class="card-photo violet" role="img" aria-label="Violet crystal globe on stand"></div><h3 class="card-title">Neque porro</h3><p class="card-text">who seeks after it and<br>wants to have it.</p></article>
  <article class="card" style="left:175px;top:350px"><div class="card-photo red" role="img" aria-label="Red crystal sphere"></div><h3 class="card-title">Neque porro</h3><p class="card-text">who seeks after it and<br>wants to have it.</p></article>
  <article class="card" style="left:335px;top:350px"><div class="card-photo clear" role="img" aria-label="Clear crystal sphere with etched figure"></div><h3 class="card-title">Neque porro</h3><p class="card-text">who seeks after it and<br>wants to have it.</p></article>
  <svg class="pager" style="left:18px;top:539px" width="10" height="12"><path d="M8 1 2 6l6 5" stroke="#999" stroke-width="2.5" fill="none"/></svg>
  <svg class="pager" style="left:451px;top:539px" width="10" height="12"><path d="M2 1l6 5-6 5" stroke="#999" stroke-width="2.5" fill="none"/></svg>
</main>

<!-- right column -->
<aside class="side" style="left:661px">
  <div class="side-head" style="margin-top:9px;height:27px">Log In</div>
  <form class="login" style="padding:16px 0 0 18px">
    <label>Log In</label><div class="field"></div>
    <label>Password</label><div class="field"></div>
    <div style="font-size:9px;display:flex;gap:18px"><a href="#" style="color:#7f8394;text-decoration:underline">Forgot Password?</a><a href="#" style="color:var(--link-red);text-decoration:underline">Sign up</a></div>
    <div style="margin:7px 0 0 79px;width:52px;height:16px;background:#dfe3f6;color:#111;font-size:10px;text-align:center;line-height:16px">Sign in</div>
  </form>
  <div class="side-head" style="margin-top:26px;height:27px">Exhibitions Coverage</div>
  <div class="thumb-row" style="margin:14px 0 0 18px"><span class="thumb"></span><p>Lorem ipsum dolor sit amet, sectetu<a class="more" href="#">more</a></p></div>
  <div class="thumb-row" style="margin:9px 0 0 18px"><span class="thumb"></span><p>Lorem ipsum dolor sit amet, sectetu<a class="more" href="#">more</a></p></div>
  <div class="thumb-row" style="margin:9px 0 0 18px"><span class="thumb"></span><p>Lorem ipsum dolor sit amet, sectetu<a class="more" href="#">more</a></p></div>
  <div style="font-family:'Cinzel',serif;font-size:9.5px;margin:26px 0 0 10px">Live Chat</div>
</aside>
<a class="chat-btn" href="#">Live Chat</a>

<footer class="site-footer">
  <div class="f-col sites" style="left:31px"><h4>Other Websites</h4><ul>
    <li>www.vellmar1glass.com</li><li>www.vellmar2glass.com</li><li>www.vellmar3glass.com</li><li>www.vellmar4glass.com</li><li>www.vellmar5glass.com</li></ul></div>
  <div class="f-col" style="left:220px"><h4>Home</h4></div>
  <div class="f-col arrows" style="left:277px"><h4 style="margin-left:11px">Facilities</h4><ul>
    <li>Factories overview</li><li>Factories image and<br>video gallery</li><li>Show rooms locator</li><li>Quality Control</li></ul></div>
  <div class="f-col arrows" style="left:413px"><h4 style="margin-left:12px">Media&nbsp; Center</h4><ul>
    <li>Press releases</li><li>Logos &amp; artwork</li><li>Media contacts</li></ul></div>
  <div class="f-col arrows" style="left:522px"><h4 style="margin-left:11px">Careers</h4><ul>
    <li>Opened positions</li><li>Candidates resumes</li></ul></div>
  <div class="f-col" style="left:654px"><h4>About Us</h4></div>
  <div class="f-col" style="left:754px;top:99px"><h4>Connect Us</h4></div>
</footer>
<div class="social"><span>Facely</span><span>Chirper</span><span class="feed">Feed</span></div>

</body>
</html>
```